Design for Chirpwall Ad to promote Laptops purchase

Need a graphic design for a Chirpwall Ad - to promote 2 laptops (PC and Zorvane) with the stated required ad-text.

AD TEXT:

FOR SME BUSINESS ONLY!
Chat with us!
To get advice on how to apply
and defray up to 80%* of business laptop purchase cost!

*Terms and Conditions apply

Image for reference only

Target Market(s)

Small medium business

Font styles to use
Sans Serif

Requirements
Must have
• 2 laptop images (see attached ) - 1 vector image of ZORVANE , and pls try to create another vector image of PC laptop (where screen is showing Blue Pendrel screen)

```html
<!DOCTYPE html>
<html lang="en">
<head>
<meta charset="utf-8">
<title>Chirpwall Ad – Business Laptops for SMEs</title>
<link rel="stylesheet" href="https://fonts.googleapis.com/css2?family=Oswald:wght@700&family=Nunito:ital,wght@0,800;0,900;1,800&display=swap">
<style>
  :root {
    --sky-deep: #1f8fd8;
    --sky-mid: #4aa9e6;
    --sky-pale: #e9f4fb;
    --white: #ffffff;
    --ink-dark: #1b222c;
    --ink-slate: #3d4c5e;
    --accent-blue: #2a90d8;
    --accent-line: #2b97e0;
    --caption-grey: #5d6670;
    --terms-blue: #3f9ee2;
  }
  * { margin: 0; padding: 0; box-sizing: border-box; }
  html, body {
    width: 1200px;
    height: 1200px;
    overflow: hidden;
    background: var(--white);
  }
  .ad-canvas {
    position: relative;
    width: 1200px;
    height: 1200px;
    overflow: hidden;
    font-family: "Nunito", Arial, sans-serif;
  }
  .sky-backdrop {
    position: absolute;
    inset: 0;
    background: linear-gradient(180deg, var(--sky-deep) 0%, var(--sky-mid) 22%, #9fd0f0 40%, var(--sky-pale) 55%, var(--white) 66%);
  }
  .base-band {
    position: absolute;
    inset: 0;
    width: 1200px;
    height: 1200px;
  }
  .headline {
    position: absolute;
    top: 108px;
    left: 0;
    width: 1200px;
    text-align: center;
    font-family: "Oswald", "Arial Narrow", sans-serif;
    font-weight: 700;
    font-size: 168px;
    line-height: 160px;
    letter-spacing: 3px;
    color: var(--white);
    text-transform: uppercase;
    text-shadow: 4px 6px 10px rgba(0, 0, 0, 0.45);
  }
  .headline span { display: block; }
  .laptop {
    position: absolute;
    border-radius: 14px 14px 6px 6px;
  }
  .laptop--zorvane {
    left: 24px;
    top: 490px;
    width: 548px;
    height: 326px;
    background: radial-gradient(ellipse at 60% 40%, #d47ac8 0%, #8a3f9c 35%, #2a1840 75%, #120c1c 100%);
  }
  .laptop--pc {
    left: 610px;
    top: 490px;
    width: 546px;
    height: 332px;
    background: linear-gradient(135deg, #39b8f5 0%, #1a8ee6 55%, #0f6fc9 100%);
  }
  .image-note {
    position: absolute;
    left: 103px;
    top: 832px;
    font-weight: 800;
    font-size: 18px;
    letter-spacing: 1.5px;
    color: var(--caption-grey);
  }
  .chat-button {
    position: absolute;
    left: 428px;
    top: 892px;
    width: 372px;
    height: 78px;
    border-radius: 20px;
    background: var(--accent-blue);
    color: var(--white);
    font-weight: 800;
    font-size: 44px;
    line-height: 78px;
    text-align: center;
  }
  .offer-copy {
    position: absolute;
    left: 0;
    top: 990px;
    width: 1200px;
    text-align: center;
    color: var(--white);
    font-weight: 800;
    font-size: 44px;
    line-height: 45px;
  }
  .terms-note {
    position: absolute;
    left: 0;
    top: 1150px;
    width: 1200px;
    text-align: center;
    color: var(--terms-blue);
    font-style: italic;
    font-weight: 800;
    font-size: 21px;
    letter-spacing: 2px;
  }
</style>
</head>
<body>
<main class="ad-canvas">
  <div class="sky-backdrop" role="img" aria-label="Blue flowing wave-line pattern fading into white"></div>

  <svg class="base-band" viewBox="0 0 1200 1200" aria-hidden="true">
    <defs>
      <linearGradient id="band-fill" x1="0" y1="1" x2="1" y2="0">
        <stop offset="0" stop-color="#3d4c5e"/>
        <stop offset="0.55" stop-color="#232b36"/>
        <stop offset="1" stop-color="#1b222c"/>
      </linearGradient>
    </defs>
    <polygon points="0,897 1200,753 1200,765 0,909" fill="#2b97e0"/>
    <polygon points="0,909 1200,765 1200,1200 0,1200" fill="url(#band-fill)"/>
  </svg>

  <h1 class="headline"><span>For SME</span><span>Business Only!</span></h1>

  <div class="laptop laptop--zorvane" role="img" aria-label="Silver Zorvane laptop with a purple and pink galaxy screen"></div>
  <div class="laptop laptop--pc" role="img" aria-label="Silver PC laptop showing a blue Pendrel desktop screen"></div>

  <p class="image-note">Images for reference only.</p>

  <div class="chat-button">Chat with us!</div>

  <p class="offer-copy">To get advice on how to apply<br>and defray up to 80%* of business laptop<br>purchase cost!</p>

  <p class="terms-note">*Terms and Conditions apply</p>
</main>
</body>
</html>
```